I need a business card design for a new dance business. I offer classical Indian dance tuition and also professional performances. I want to offer the community a variety of Indian dance experiences which include: group class and private tuition, school and preschool educational courses and workshops. dance theatre performances, community function workshops and performances, Kids Bollywood parties, wedding & conference performances, mouth percussion classes, Indian mythology/ dance costume and make up workshops.
The final design should communicate a feeling and impression of the vibrance and energy of Indian dance.
Updates
Hi Everyone,
Project Deadline Extended
Reason: I would like to refine a few changes to the details of this lovely design and we have run out of time!
Project Deadline Extended
Reason: Still waiting to hear back form designer re two possible changes to the card design. Tomorrow is the deadline and I have sent several messages but with no response. I need to see this through before selecting this lovely design.
Thank you.
Tara
Industry/Entity Type
Preschool
Requirements
Must have
- The front of the business card should have the photo of me (my face and torso), surrounded entirely by a border of bright magenta (to match the magenta of my lipstick - it is the same as the magenta on my skirt in the second photo). Within the top border I want (perhaps yellow-gold) writing to say "Tara Holloway - Artistic Director" and within the bottom border it should read "Silver Creek Kathak Studio." If you turn the card on its side the left border should have my telephone number: 0417 826 394 and the right-hand border should read: silvercreekkathakstudio@fernmail.example
The reverse of the card should be the orange of the dance costume
and I'd like the picture of my feet and legs to be on the right side of the back of the card as a side border. Centre-aligned on the orange background it should read (perhaps in dark magenta):
Indian dance classes + private tuition
School + preschool educational courses and workshops
Dance theatre performances
Community function workshops and performances
Children's Bollywood parties
Wedding + conference performances
Mouth percussion classes
Indian mythology and dance demonstration workshops
Dance costume and make-up workshops
Nice to have
- A lovely artistic but easy-to-read font would be nice.

```html
<!DOCTYPE html>
<html lang="en">
<head>
<meta charset="utf-8">
<title>Silver Creek Kathak Studio – Business Card</title>
<link rel="stylesheet" href="https://fonts.googleapis.com/css2?family=Open+Sans:wght@600;700;800&display=swap">
<style>
  :root {
    --page-orange: #f7a21c;
    --page-orange-light: #fbc03e;
    --card-gold: #fdb827;
    --card-gold-light: #ffd35a;
    --magenta: #8e1846;
    --magenta-deep: #6a0f33;
    --magenta-bright: #b0235d;
    --label-band: #7a1238;
    --gold-text: #ffd23a;
    --cream-text: #fff2a6;
    --dark-text: #3a1606;
  }
  * { margin: 0; padding: 0; box-sizing: border-box; }
  html, body { width: 1024px; height: 1200px; overflow: hidden; }
  body {
    position: relative;
    font-family: "Open Sans", Arial, sans-serif;
    background: linear-gradient(180deg, var(--page-orange-light), var(--page-orange));
  }

  .card {
    position: absolute;
    left: 24px;
    width: 976px;
    border-radius: 18px;
    overflow: hidden;
    background: linear-gradient(180deg, var(--card-gold-light), var(--card-gold));
    box-shadow: 0 4px 10px rgba(120, 60, 0, 0.25);
  }

  /* Front */
  .card-front { top: 15px; height: 572px; }
  .front-title {
    position: absolute; top: 0; left: 0; right: 0; height: 88px;
    display: flex; align-items: center; justify-content: center;
    font-weight: 700; font-size: 34px; color: var(--dark-text);
  }
  .front-frame {
    position: absolute; left: 29px; top: 88px; width: 918px; height: 469px;
    border-radius: 6px;
    background: radial-gradient(ellipse at 50% 45%, var(--magenta-bright), var(--magenta) 55%, var(--magenta-deep));
  }
  .portrait {
    position: absolute; left: 303px; top: 0; width: 372px; height: 420px;
    background: radial-gradient(ellipse at 50% 40%, #f1d6c6 0%, #d9a77e 45%, #b06a3a 75%, var(--magenta) 100%);
  }
  .front-label {
    position: absolute; left: 225px; top: 412px; width: 468px; height: 52px;
    background: var(--label-band);
    display: flex; align-items: center; justify-content: center;
    font-weight: 700; font-size: 32px; color: var(--gold-text);
    border-radius: 4px;
  }

  /* Back */
  .card-back { top: 616px; height: 570px; }
  .back-side-name {
    position: absolute; left: 66px; top: 0; height: 570px;
    writing-mode: vertical-rl; transform: rotate(180deg);
    display: flex; align-items: center; justify-content: center;
    font-weight: 800; font-size: 31px; color: var(--magenta-deep);
  }
  .services {
    position: absolute; left: 94px; top: 74px; width: 600px;
    list-style: none; text-align: center;
    font-weight: 700; font-size: 26px; line-height: 34px;
    color: var(--cream-text);
  }
  .dancer-feet {
    position: absolute; left: 704px; top: 14px; width: 236px; height: 540px;
    background: linear-gradient(180deg, #c21f6a 0%, #9c1a55 35%, #e08a2a 60%, #c96d34 80%, #8f4a22 100%);
    border-radius: 40% 40% 10% 10% / 12% 12% 4% 4%;
  }
  .back-email {
    position: absolute; right: 10px; top: 0; height: 570px;
    writing-mode: vertical-rl;
    display: flex; align-items: center; justify-content: center;
    font-weight: 700; font-size: 22px; color: var(--magenta-deep);
  }
</style>
</head>
<body>
  <section class="card card-front">
    <h1 class="front-title">Tara Holloway - Artistic Director</h1>
    <div class="front-frame">
      <div class="portrait" role="img" aria-label="Photo of the dancer in classical Indian costume and headdress, face and torso"></div>
      <div class="front-label">Silver Creek Kathak Studio</div>
    </div>
  </section>

  <section class="card card-back">
    <div class="back-side-name">Silver Creek Kathak Studio</div>
    <ul class="services">
      <li>Indian dance classes + private tuition</li>
      <li>School + preschool educational courses<br>and workshops</li>
      <li>Dance theatre performances</li>
      <li>Community function workshops and<br>performances</li>
      <li>Children's Bollywood parties</li>
      <li>Wedding + conference performances</li>
      <li>Mouth percussion classes</li>
      <li>Indian mythology and dance<br>demonstration workshops</li>
      <li>Dance costume and make-up workshops</li>
    </ul>
    <div class="dancer-feet" role="img" aria-label="Photo of the dancer's legs and feet in a magenta and orange skirt"></div>
    <div class="back-email">silvercreekkathakstudio@fernmail.example</div>
  </section>
</body>
</html>
```